Mechanical Engineer Business Card Design (Unemployed)

I am unemployed and actively looking for a job in Canada. I will be using this business card when I meet potential employers or in networking events.I would love to have the engraved writing style (as if it is engraved on the card). Some examples attached.I would love to have a personalized logo that represents my 2 majors. The final design should have a professional look that can stand out if attached to a resume. Jobs I am applying for are in construction, mining, oil and gas, Aerospace, manufacturing and whatever field I can be integrated in.A metallic look on the back is ok. but the front have to be sort of can be written on. you can also try to add my profilelink profile https://ca.profilelink.example/in/tomasvelder
On the front or back, I would love to have the symbol of mail and phone rather than the words. that saves spaceAmaze me guys.

Target Market(s)

Engineering

Industry/Entity Type

Engineering

Contact Information for Business Card

Tomas Velder
Mechanical Engineer

Phone number: +1 (555) 014 - 2738
email: veldertomas@mailbox.example

Requirements
Must have
• PERSONALIZED and brand new Simple Logo
• Professional look
• Engraved writing for the name
• Help stand out when attached on CV
Nice to have
• Metallic back look

```html
<!DOCTYPE html>
<html lang="en">
<head>
<meta charset="utf-8">
<title>Tomas Velder — Business Card</title>
<link rel="stylesheet" href="https://fonts.googleapis.com/css2?family=Courier+Prime:wght@400;700&family=Tinos&display=swap">
<style>
  :root {
    --backdrop: #dcdcdc;
    --card-light: #fbfafa;
    --card-dark: #000000;
    --ink: #111111;
    --ink-soft: #222222;
    --paper: #ffffff;
  }
  * { box-sizing: border-box; margin: 0; padding: 0; }
  html, body {
    width: 1189px;
    height: 1200px;
    overflow: hidden;
    background: var(--backdrop);
  }
  .canvas {
    position: relative;
    width: 1189px;
    height: 1200px;
  }
  .card {
    position: absolute;
    left: 140px;
    width: 917px;
    height: 524px;
    overflow: hidden;
  }
  .card--front {
    top: 45px;
    background: var(--card-light);
  }
  .card--back {
    top: 624px;
    background: var(--card-dark);
  }
  .corner-ring {
    position: absolute;
    left: 607px;
    top: -89px;
    width: 440px;
    height: 440px;
    border-radius: 50%;
    border: 28px solid var(--ink);
  }
  .holder-name {
    position: absolute;
    left: 72px;
    top: 104px;
    font-family: "Courier Prime", "Courier New", monospace;
    font-weight: 700;
    font-size: 50px;
    letter-spacing: 0.5px;
    color: var(--ink);
    text-shadow: 0 1px 1px rgba(255,255,255,0.9), 0 -1px 2px rgba(0,0,0,0.35), 0 2px 4px rgba(0,0,0,0.18);
  }
  .credentials {
    position: absolute;
    left: 72px;
    top: 175px;
    list-style: none;
    font-family: "Tinos", "Times New Roman", serif;
    font-size: 25px;
    line-height: 31px;
    color: var(--ink-soft);
  }
  .contact {
    position: absolute;
    left: 72px;
    top: 378px;
    list-style: none;
    font-family: "Tinos", "Times New Roman", serif;
    font-size: 25px;
    color: var(--ink-soft);
  }
  .contact__item {
    display: flex;
    align-items: center;
    height: 46px;
  }
  .contact__icon {
    width: 21px;
    height: 21px;
    margin-right: 29px;
    flex: none;
  }
  .back-mark {
    position: absolute;
    left: 271px;
    top: 81px;
    width: 360px;
    height: 360px;
    border-radius: 50%;
    border: 26px solid var(--paper);
    display: flex;
    align-items: center;
    justify-content: center;
  }
  .back-mark__name {
    font-family: "Courier Prime", "Courier New", monospace;
    font-weight: 700;
    font-size: 40px;
    color: var(--paper);
    text-align: center;
    line-height: 1.1;
  }
</style>
</head>
<body>
<main class="canvas">
  <section class="card card--front" aria-label="Business card front">
    <div class="corner-ring" aria-hidden="true"></div>
    <h1 class="holder-name">Tomas Velder</h1>
    <ul class="credentials">
      <li>Field Mechanical Engineer</li>
      <li>Mechanical Engineer (B.Sc.)</li>
      <li>Aerospace Engineer (M.Sc.)</li>
    </ul>
    <ul class="contact">
      <li class="contact__item">
        <svg class="contact__icon" viewBox="0 0 21 21" aria-label="Phone" role="img">
          <rect width="21" height="21" fill="#111"/>
          <path d="M6 4.5c1-.6 1.6-.4 2.1.6l.9 1.9c.3.7.1 1.2-.5 1.6l-.7.4c.6 1.6 1.7 2.9 3.2 3.8l.5-.6c.5-.5 1-.6 1.6-.2l1.7 1.1c.8.5.9 1.2.2 2-1 1.2-2.2 1.4-3.6.7C8.6 14.4 6.4 11.8 5.4 8.7 5 7 5.1 5.3 6 4.5z" fill="#fff"/>
        </svg>
        <span>(+1) 555 - 014 - 2738</span>
      </li>
      <li class="contact__item">
        <svg class="contact__icon" viewBox="0 0 21 21" aria-label="Email" role="img">
          <rect width="21" height="21" fill="#111"/>
          <rect x="4" y="6" width="13" height="9" fill="#fff"/>
          <path d="M4 6l6.5 5L17 6M4 15l4.5-4.5M17 15l-4.5-4.5" stroke="#111" stroke-width="1.1" fill="none"/>
        </svg>
        <span>veldertomas@mailbox.example</span>
      </li>
    </ul>
  </section>

  <section class="card card--back" aria-label="Business card back">
    <div class="back-mark">
      <span class="back-mark__name">Tomas<br>Velder</span>
    </div>
  </section>
</main>
</body>
</html>
```